Business Card Design

My business will be called TB Carpentry & Renovations. I am a liscenced carpentar who specialises in renovations/alterations/refurbishments and maintenance. I have experience in all types of Carpentry tho. I also have experience in tiling, painting and concrete which obviously gives me an edge in the refurbishment market for building. But i am not liscenced in these trades. I pride myself on being an honest and very reliable. There are alot of tradesman where i live who are not reliable so i really want to let the community know they can trust me and that i am willing to do all types of work.
I would like to see design and is not over the top but uses earthy/modern colours which presents a down to earth message.

I would really like to communicate diversity, reliabilty and quality work.

I have attached a couple of concepts i have come up with PrintNest, These may aid you.
Updates

Industry/Entity Type

Painting

Contact Information for Business Card

Name: Dean Holloway
Email: dean.holl@examplemail.net
Ph: 0418552916

Requirements
Must have
• Licence No: 581937K

```html
<!DOCTYPE html>
<html lang="en">
<head>
<meta charset="utf-8">
<title>TB Carpentry &amp; Renovations — Business Card</title>
<link rel="stylesheet" href="https://fonts.googleapis.com/css2?family=Noto+Sans:wght@400;700&display=swap">
<style>
  :root {
    --brand-blue: #1a74b4;
    --card-white: #f7f8f8;
    --panel-grey: #d9dadb;
    --ink: #1d1d1f;
    --stage: #e9eaec;
  }
  * { box-sizing: border-box; margin: 0; padding: 0; }
  html, body { width: 1200px; height: 901px; overflow: hidden; }
  body {
    background: var(--stage);
    font-family: "Noto Sans", Verdana, sans-serif;
    position: relative;
  }
  .card {
    position: absolute;
    top: 296px;
    width: 540px;
    height: 309px;
    overflow: hidden;
    box-shadow: 0 6px 18px rgba(0,0,0,.18);
  }
  .card--front { left: 40px; background: var(--card-white); }
  .card--back { left: 620px; background: var(--brand-blue); }
  .card__edges { position: absolute; inset: 0; }

  .services {
    position: absolute;
    right: 34px; top: 36px;
    text-align: right;
    color: var(--brand-blue);
    font-weight: 700;
    font-size: 14px;
    line-height: 1.45;
  }
  .services__lead { margin-bottom: 2px; }

  .contact {
    position: absolute;
    left: 34px; top: 116px;
    color: var(--ink);
    font-size: 14px;
    line-height: 1.3;
  }
  .contact__name { color: var(--brand-blue); font-weight: 700; font-size: 17px; margin-bottom: 6px; }
  .contact__licence { font-size: 11.5px; }

  .brand-name {
    position: absolute;
    left: 34px; top: 214px;
    display: flex;
    align-items: center;
    gap: 12px;
    color: var(--brand-blue);
    font-weight: 700;
    font-size: 22px;
    line-height: 1.1;
  }
  .brand-name__mark {
    width: 40px; height: 40px;
    background: var(--brand-blue);
    flex: none;
  }

  .back-header {
    position: absolute;
    left: 0; right: 0; top: 18px;
    text-align: center;
    color: #fff;
    font-size: 15px;
    line-height: 1.3;
  }
  .appointment {
    position: absolute;
    left: 56px; right: 30px; top: 78px; bottom: 28px;
    background: var(--panel-grey);
    padding: 16px 24px;
    color: var(--ink);
    font-size: 14px;
  }
  .appointment__title {
    color: var(--brand-blue);
    font-weight: 700;
    font-size: 17px;
    text-align: center;
    margin-bottom: 12px;
  }
  .appointment__row { display: flex; align-items: flex-end; gap: 8px; margin-bottom: 18px; }
  .appointment__line { flex: 1; border-bottom: 1.5px solid var(--ink); height: 15px; }
  .appointment__note { text-align: center; line-height: 1.45; margin-top: 14px; }
</style>
</head>
<body>

<section class="card card--front" aria-label="Business card front">
  <svg class="card__edges" viewBox="0 0 540 309" preserveAspectRatio="none" aria-hidden="true">
    <polygon points="0,0 120,0 0,42" fill="var(--brand-blue)"/>
    <polygon points="540,238 540,309 300,309 312,296 520,286 524,242" fill="var(--brand-blue)"/>
  </svg>
  <div class="services">
    <div class="services__lead">Carpentry &amp; All Building Services</div>
    <div>Renovations</div>
    <div>Maintenance</div>
    <div>General Repairs</div>
  </div>
  <div class="contact">
    <div class="contact__name">Dean Holloway</div>
    <div>0418552916</div>
    <div>dean.holl@examplemail.net</div>
    <div class="contact__licence">Licence Nº: 581937K</div>
  </div>
  <div class="brand-name">
    <span class="brand-name__mark" aria-hidden="true"></span>
    <span>TB Carpentry<br>&amp; Renovations</span>
  </div>
</section>

<section class="card card--back" aria-label="Business card back">
  <div class="back-header">
    <div>Carpentry &amp; All Building Services</div>
    <div>Renovations • Maintenance • General Repairs</div>
  </div>
  <div class="appointment">
    <div class="appointment__title">Appointment</div>
    <div class="appointment__row">
      <span>Date</span><span class="appointment__line"></span>
      <span>Time</span><span class="appointment__line"></span>
    </div>
    <div class="appointment__row">
      <span>For</span><span class="appointment__line"></span>
    </div>
    <p class="appointment__note">This time is reserved for you. 24 hours notice<br>is appreciated for rescheduling your appointment.</p>
  </div>
</section>

</body>
</html>
```